Plantain chip snack pack bag design + company logo design

We need to design a bag for a new snack food company. The brand is called "Crunch Bloom," and the first product, plantain chips, will come in 4 flavors - Classic Unripe, Sweet 'n Spicy!!, Original Sweet, and Ginger & Soy. The bag - which we plan to print in multiple sizes - needs to have a clear section on the front so the contents are visible, as they will be sold by street vendors and ability to view the contents is key. Design needs to be "very happy and exciting" and feature simple, strong colors that say "delicious and crispy" i.e. Classic Unripe is green, Sweet 'n Spicy!! is red, Original Sweet is yellow, and Ginger & Soy is tan (plus these will be printed in mass so must be simple yet very catchy on shelves and on the street vendors). On the back, there needs to be a column of nutritional content, plus the company contact address, email, phone lines, Twitter/Facebook/Instagram handles, and the quality certification number. Also, on the back, a bar code and "Made in xxx" text. Finally, the net weight of contents needs to be on the front as well. I have uploaded a sample of a competing product's packaging as inspiration only (NOT TO BE COPIED but to our design MUST BE MORE CATCHY, ATTRACTIVE, and FUN than this one)

Target Market(s)

All snack consumers, especially those with a bias toward healthier eating.

Industry/Entity Type

It Company

Logo Text

Delight in every bite!

Font styles to use
Serif
Decorative
Script

Requirements
Must have
• 1. For the package design, handoffs must include placeholders for ALL text so we can edit the text as needed
• 2. For package design, large transparent section on bag is critical so contents are visible; also, branding of "Crunch Bloom" must be large and recognizable from a distance
• 3. Primary colors suitable for industrial mass production
• 4. Logo design on the bags must include the parent company name i.e. "Crunch Bloom Snacks by Tolvaro Foods"
• 5. Package must say "Plantain chips" and the flavor e.g. "Sweet 'n Spicy!!" and with a small image of a hot pepper (each flavor should have a similar small image representing the flavor)
• 6. For the Logo design portion of the project, the Tolvaro Foods Limited logo should incorporate plantains, coconuts, potatos and corn. This logo is for the parent company and Crunch Bloom is the plantain chip product line
Nice to have
• 1. Smiling faces suggesting happiness, health, friendliness, and overall delight at eating the chips

```html
<!DOCTYPE html>
<html lang="en">
<head>
<meta charset="utf-8">
<title>Crunch Bloom Plantain Chips – Sweet 'n Spicy!! Pack</title>
<link rel="stylesheet" href="https://fonts.googleapis.com/css2?family=Caprasimo&family=Montserrat:wght@600;700;800;900&display=swap">
<style>
  :root {
    --canvas-bg: #e6e6e6;
    --seal-red: #c8231a;
    --seal-red-dark: #8f160f;
    --brand-green: #34500e;
    --sun-yellow: #ffe81a;
    --sun-light: #fff8b0;
    --sun-deep: #f7c800;
    --flavour-red: #d62a1e;
    --flavour-red-dark: #a51c13;
    --cream: #fff6d2;
    --pepper-red: #e0301f;
    --pepper-green: #3f7a1c;
    --chip-gold: #dba526;
    --chip-light: #f3cf55;
    --chip-dark: #a8720f;
  }
  * { margin: 0; padding: 0; box-sizing: border-box; }
  html, body {
    width: 1200px; height: 900px; overflow: hidden;
    background: var(--canvas-bg);
    font-family: "Montserrat", Arial, sans-serif;
  }
  .canvas { position: relative; width: 1200px; height: 900px; }

  .bag {
    position: absolute; left: 350px; top: 100px;
    width: 500px; height: 703px;
    display: flex; flex-direction: column;
    box-shadow: 0 18px 30px rgba(0,0,0,0.18);
  }
  .seal {
    background: linear-gradient(180deg, var(--seal-red) 0%, var(--seal-red-dark) 100%);
    position: relative; flex: none;
  }
  .seal--top { height: 60px; }
  .seal--bottom { height: 55px; }
  .hang-hole {
    position: absolute; left: 218px; top: 18px;
    width: 64px; height: 18px; border-radius: 9px;
    background: #fafafa;
  }

  .front-label {
    height: 300px; flex: none; position: relative;
    background: radial-gradient(ellipse 75% 80% at 50% 40%, var(--sun-light) 0%, var(--sun-yellow) 50%, var(--sun-deep) 100%);
  }
  .brand-name {
    position: absolute; left: 0; right: 0; top: 14px;
    text-align: center;
    font-family: "Caprasimo", Georgia, serif; font-weight: 400;
    font-size: 62px; line-height: 62px;
    color: var(--brand-green);
  }
  .brand-name span { display: block; }
  .brand-owner {
    position: absolute; left: 0; right: 0; top: 146px;
    text-align: center; font-size: 13px; font-weight: 700;
    letter-spacing: 3px; color: var(--brand-green);
  }
  .product-name {
    position: absolute; left: 0; right: 0; top: 172px;
    text-align: center; font-weight: 900; font-size: 36px; line-height: 44px;
    color: var(--brand-green); letter-spacing: 0.5px;
  }
  .flavour-band {
    position: absolute; left: 0; right: 0; top: 228px; height: 44px;
    background: linear-gradient(180deg, var(--flavour-red) 0%, var(--flavour-red-dark) 100%);
    display: flex; align-items: center; padding-left: 40px;
  }
  .flavour {
    font-weight: 800; font-size: 21px; letter-spacing: 3px;
    color: var(--cream);
  }
  .flavour-icon {
    position: absolute; right: 34px; top: 214px; z-index: 2;
    width: 72px; height: 72px; border-radius: 50%;
    background: var(--cream); border: 3px solid var(--flavour-red-dark);
    display: flex; align-items: center; justify-content: center;
  }
  .flavour-icon__art {
    width: 44px; height: 44px; border-radius: 50%;
    background: radial-gradient(circle at 40% 40%, var(--pepper-red) 0%, var(--pepper-red) 55%, var(--pepper-green) 100%);
  }

  .clear-window {
    height: 215px; flex: none;
    background:
      radial-gradient(circle at 20% 35%, var(--chip-light) 0%, transparent 18%),
      radial-gradient(circle at 60% 60%, var(--chip-light) 0%, transparent 20%),
      radial-gradient(circle at 85% 25%, var(--chip-light) 0%, transparent 14%),
      linear-gradient(180deg, var(--chip-gold) 0%, var(--chip-dark) 100%);
  }

  .info-strip {
    height: 73px; flex: none; position: relative;
    background: linear-gradient(90deg, var(--sun-deep) 0%, var(--sun-yellow) 40%, var(--sun-light) 100%);
  }
  .net-weight {
    position: absolute; left: 28px; top: 14px; width: 80px;
    color: var(--brand-green); text-align: center;
  }
  .net-weight__label { font-size: 10px; font-weight: 800; }
  .net-weight__value { font-size: 27px; font-weight: 900; line-height: 30px; }
  .info-copy {
    position: absolute; left: 126px; top: 10px; width: 350px;
    font-size: 9.5px; font-weight: 600; line-height: 12px;
    color: var(--brand-green);
  }
  .website {
    position: absolute; left: 126px; top: 48px;
    font-size: 13.5px; font-weight: 800;
    color: var(--brand-green);
  }
</style>
</head>
<body>
<main class="canvas">
  <article class="bag">
    <div class="seal seal--top"><div class="hang-hole"></div></div>

    <section class="front-label">
      <h1 class="brand-name"><span>Crunch</span><span>Bloom</span></h1>
      <p class="brand-owner">SNACKS BY TOLVARO FOODS</p>
      <h2 class="product-name">PLANTAIN CHIPS</h2>
      <div class="flavour-band"><p class="flavour">SWEET ‘N SPICY!!</p></div>
      <div class="flavour-icon"><div class="flavour-icon__art" role="img" aria-label="Small hot pepper picture for the flavour"></div></div>
    </section>

    <div class="clear-window" role="img" aria-label="Clear window showing golden plantain chips inside the bag"></div>

    <section class="info-strip">
      <div class="net-weight">
        <div class="net-weight__label">NET. WEIGHT</div>
        <div class="net-weight__value">80g</div>
      </div>
      <p class="info-copy">Lorem ipsum dolor sit amet, consectetur adipisicing elit, sed do eiusmod tempor incididunt ut labore et dolore magna aliqua. Ut enim ad minim veniam.</p>
      <p class="website">WWW.CRUNCHBLOOMSNACKS.COM</p>
    </section>

    <div class="seal seal--bottom"></div>
  </article>
</main>
</body>
</html>
```